" buscamos elaborar produtos saudáveis, isentos de glúten, lactose e açúcar. E utilizando ingredientes benéficos a nossa saúde, como fibra e gorduras boas (insaturadas). "

```html
<!DOCTYPE html>
<html lang="pt-BR">
<head>
<meta charset="UTF-8">
<title>Campo Leve – Adesivos</title>
<link rel="stylesheet" href="https://fonts.googleapis.com/css2?family=Nunito:wght@500&family=Open+Sans:wght@400&display=swap">
<style>
  :root {
    --backdrop: #ece7df;
    --paper: #ffffff;
    --leaf-green: #8cb43c;
    --ring-green: #6f9a2a;
    --citrus-orange: #ee7b22;
    --ink: #3a3a3a;
  }
  * { margin: 0; padding: 0; box-sizing: border-box; }
  html, body {
    width: 1200px;
    height: 1200px;
    overflow: hidden;
    background: var(--backdrop);
  }
  .canvas {
    position: relative;
    width: 1200px;
    height: 1200px;
  }
  .sticker {
    position: absolute;
    background: var(--paper);
    display: flex;
    flex-direction: column;
    align-items: center;
    text-align: center;
  }
  .sticker--round {
    left: 110px;
    top: 144px;
    width: 466px;
    height: 466px;
    border-radius: 50%;
    border: 13px solid var(--ring-green);
    padding-top: 118px;
  }
  .sticker--square {
    left: 631px;
    top: 643px;
    width: 461px;
    height: 480px;
    border: 6px solid var(--citrus-orange);
    border-right-width: 16px;
    border-bottom-width: 16px;
    padding-top: 150px;
  }
  .brand-dot {
    width: 92px;
    height: 92px;
    border-radius: 50%;
    background: var(--citrus-orange);
  }
  .brand-name {
    margin-top: 28px;
    font-family: "Nunito", sans-serif;
    font-weight: 500;
    font-size: 54px;
    line-height: 1;
    color: var(--leaf-green);
    letter-spacing: -0.5px;
  }
  .contact {
    font-family: "Open Sans", sans-serif;
    font-weight: 400;
    font-size: 21px;
    line-height: 34px;
    color: var(--ink);
  }
  .contact--round { margin-top: 24px; }
  .contact--square { margin-top: 22px; font-size: 22px; }
</style>
</head>
<body>
  <main class="canvas">
    <section class="sticker sticker--round">
      <div class="brand-dot"></div>
      <h1 class="brand-name">Campo Leve</h1>
      <div class="contact contact--round">
        <p class="contact-phone">21 90417-2286</p>
        <p class="contact-email">campoleve@exemplo.com</p>
      </div>
    </section>

    <section class="sticker sticker--square">
      <div class="brand-dot"></div>
      <h2 class="brand-name">Campo Leve</h2>
      <div class="contact contact--square">
        <p class="contact-phone">21 90417-2286</p>
        <p class="contact-email">campoleve@exemplo.com</p>
      </div>
    </section>
  </main>
</body>
</html>
```